Business Card for a Wedding Films Business

We require a business card design for our business 'Lewis Marrow Wedding Films'. The logo needs to look classy and high end.

Target Market(s)

Wedding Couples

Contact Information for Business Card

Lewis Marrow Wedding Films
07312 605 227
films@lewismarrowreels.com
www.lewismarrowreels.com

Facebook: @lewismarrowweddingfilms
Instagram: @lewismarrowfilms

Font styles to use
Sans Serif

Requirements
Must have
• Social media icons - Facebook and Instagram

```html
<!DOCTYPE html>
<html lang="en">
<head>
<meta charset="utf-8">
<title>Lewis Marrow Wedding Films – Business Card</title>
<link href="https://fonts.googleapis.com/css2?family=Lato:wght@400;700&display=swap" rel="stylesheet">
<style>
  :root {
    --backdrop: #c8e6dd;
    --card-white: #ffffff;
    --card-black: #0c0c0c;
    --ink: #111111;
    --ink-soft: #2a2a2a;
    --faint-shape: #e6e6e6;
    --faint-shape-dark: #1c1c1c;
    --grey-text: #8a8a8a;
    --rule: #111111;
  }
  * { box-sizing: border-box; margin: 0; padding: 0; }
  html, body {
    width: 1200px;
    height: 856px;
    overflow: hidden;
    background: var(--backdrop);
    font-family: 'Lato', sans-serif;
    color: var(--ink);
  }
  .sheet {
    position: relative;
    width: 1200px;
    height: 856px;
    display: flex;
    align-items: center;
    justify-content: center;
    gap: 60px;
  }
  .card {
    position: relative;
    width: 500px;
    height: 300px;
    border-radius: 34px;
    overflow: hidden;
    box-shadow: 0 10px 28px rgba(0, 0, 0, 0.12);
  }
  .card--front { background: var(--card-white); }
  .card--back { background: var(--card-black); }

  .card__accent {
    position: absolute;
    left: 0;
    top: 40px;
    width: 120px;
    height: 200px;
    background: var(--faint-shape);
  }
  .card--back .card__accent { background: var(--faint-shape-dark); }

  .brand {
    position: absolute;
    text-align: center;
    font-weight: 400;
  }
  .brand__mark {
    display: block;
    width: 30px;
    height: 30px;
    margin: 0 auto 10px;
    border: 2px solid var(--ink);
  }
  .brand__name {
    display: block;
    font-size: 24px;
    letter-spacing: 6px;
    text-transform: uppercase;
    line-height: 1;
  }
  .brand__tag {
    display: block;
    font-size: 11px;
    letter-spacing: 6px;
    text-transform: uppercase;
    margin-top: 6px;
  }
  .card--front .brand { left: 150px; top: 48px; width: 310px; color: var(--ink); }
  .card--back .brand { left: 150px; top: 70px; width: 310px; color: var(--grey-text); }
  .card--back .brand__mark { border-color: var(--grey-text); }

  .rule {
    position: absolute;
    height: 2px;
    background: var(--rule);
  }
  .rule--top { left: 200px; right: 30px; top: 148px; }
  .rule--bottom { left: 34px; right: 30px; top: 236px; }

  .contact {
    position: absolute;
    list-style: none;
    font-size: 13px;
    line-height: 20px;
    color: var(--ink-soft);
  }
  .contact li { display: flex; align-items: center; gap: 8px; }
  .contact svg { flex: none; }
  .contact--direct { left: 300px; top: 160px; }
  .contact--social { left: 34px; top: 244px; }
  .social-dot {
    display: inline-block;
    width: 11px;
    height: 11px;
    background: var(--ink);
    border-radius: 2px;
  }

  .card__web {
    position: absolute;
    left: 0;
    right: 0;
    bottom: 56px;
    text-align: center;
    font-size: 12px;
    color: #ffffff;
    letter-spacing: 0.3px;
  }
</style>
</head>
<body>
<main class="sheet">
  <section class="card card--front" aria-label="Business card front">
    <div class="card__accent" aria-hidden="true"></div>
    <div class="brand">
      <span class="brand__mark" aria-hidden="true"></span>
      <span class="brand__name">Lewis Marrow</span>
      <span class="brand__tag">Wedding Films</span>
    </div>
    <div class="rule rule--top"></div>
    <ul class="contact contact--direct">
      <li>
        <svg width="10" height="14" viewBox="0 0 10 14" aria-hidden="true"><rect x="1" y="0.75" width="8" height="12.5" rx="1.3" fill="none" stroke="#111" stroke-width="1.3"/><line x1="4" y1="11" x2="6" y2="11" stroke="#111" stroke-width="1.2"/></svg>
        07312 605 227
      </li>
      <li>
        <svg width="12" height="10" viewBox="0 0 12 10" aria-hidden="true"><rect x="0.5" y="0.5" width="11" height="9" fill="#111"/><polyline points="0.8,1 6,5.5 11.2,1" fill="none" stroke="#fff" stroke-width="1"/></svg>
        films@lewismarrowreels.com
      </li>
    </ul>
    <div class="rule rule--bottom"></div>
    <ul class="contact contact--social">
      <li><span class="social-dot" aria-hidden="true"></span>@lewismarrowweddingfilms</li>
      <li><span class="social-dot" aria-hidden="true"></span>@lewismarrowfilms</li>
    </ul>
  </section>

  <section class="card card--back" aria-label="Business card back">
    <div class="card__accent" aria-hidden="true"></div>
    <div class="brand">
      <span class="brand__mark" aria-hidden="true"></span>
      <span class="brand__name">Lewis Marrow</span>
      <span class="brand__tag">Wedding Films</span>
    </div>
    <p class="card__web">www.lewismarrowreels.com</p>
  </section>
</main>
</body>
</html>
```